2.875 x 4 inch Ad for a Program Guide at Conference with 15,000

The ad needs to be 2.875 inches by 4 inches. I have attached some ideas. We definitely don't want a white background but we need the ad to visually jump off a page so our ad doesn't get lost. The mock-ups were something I put together so I could get a sense of what I wanted to say. I've also attached feedback from my business partners about these mock-ups.

Target Market(s)

Heads of Human Resources and Leadership Development, CEO's, COO's, and business owners.

Industry/Entity Type

Consulting

Font styles to use
Serif

Colors
6b449b
0355a3
0692cd
00a990
a64599
f37122

Requirements
Must have
• Colors from brand standards. Logo. Large lettering to be seen easily as a quarter page ad.
Nice to have
• Creativity... feeling of strength, warmth and business all at the same time.
Should not have
• Please note the updated logo. The name of the company is Vorrada Mindful Business.

```html
<!DOCTYPE html>
<html lang="en">
<head>
<meta charset="utf-8">
<title>Vorrada Mindful Business – Program Guide Ad Options</title>
<link rel="stylesheet" href="https://fonts.googleapis.com/css2?family=Montserrat:wght@600;800;900&family=Roboto+Condensed:ital,wght@0,400;0,700;1,700&display=swap">
<style>
  :root {
    --board: #2c2c2c;
    --navy: #0b4a8e;
    --blue: #0355a3;
    --sky: #0692cd;
    --teal: #00a990;
    --purple: #6b449b;
    --magenta: #a64599;
    --orange: #f37122;
    --cream: #f6efe0;
    --white: #ffffff;
    --ink: #1c1c1c;
  }
  * { margin: 0; padding: 0; box-sizing: border-box; }
  html, body { width: 1200px; height: 817px; overflow: hidden; background: var(--board); }
  .board { position: relative; width: 1200px; height: 817px; font-family: "Roboto Condensed", Arial, sans-serif; color: var(--white); }
  .option-label { position: absolute; top: 38px; width: 200px; text-align: center; font-size: 18px; font-weight: 400; letter-spacing: 0.2px; }
  .option-label.first { left: 212px; }
  .option-label.second { left: 773px; }
  .ad { position: absolute; top: 84px; width: 423px; height: 587px; box-shadow: 0 6px 18px rgba(0,0,0,0.55); }
  .ad.first { left: 116px; }
  .ad.second { left: 662px; }
  .ad svg { display: block; width: 423px; height: 587px; }
  .caption { position: absolute; top: 726px; left: 0; width: 1200px; text-align: center; font-size: 30px; font-weight: 400; }
  .brand-name { font-family: "Montserrat", Arial, sans-serif; font-weight: 600; fill: var(--blue); }
  .headline { font-family: "Montserrat", Arial, sans-serif; font-weight: 900; }
  .condensed { font-family: "Roboto Condensed", Arial, sans-serif; font-weight: 700; }
  .condensed-italic { font-family: "Roboto Condensed", Arial, sans-serif; font-weight: 700; font-style: italic; }
  .url { font-family: "Montserrat", Arial, sans-serif; font-weight: 800; fill: var(--white); }
</style>
</head>
<body>
<main class="board">
  <p class="option-label first">SAMPLE 1</p>
  <p class="option-label second">SAMPLE 2</p>

  <!-- Option one -->
  <section class="ad first">
    <svg viewBox="0 0 423 587" xmlns="http://www.w3.org/2000/svg">
      <defs>
        <linearGradient id="warmSky" x1="0" y1="0" x2="0" y2="1">
          <stop offset="0" stop-color="#f3e9d2"/>
          <stop offset="0.4" stop-color="#f6f3ea"/>
          <stop offset="0.62" stop-color="#c8f0ee"/>
          <stop offset="1" stop-color="#6fe0dc"/>
        </linearGradient>
        <linearGradient id="bandPurple" x1="0" y1="0" x2="1" y2="0">
          <stop offset="0" stop-color="#57347f"/>
          <stop offset="0.6" stop-color="#6b449b"/>
          <stop offset="1" stop-color="#5a3787"/>
        </linearGradient>
        <linearGradient id="teamTones" x1="0" y1="0" x2="1" y2="0">
          <stop offset="0" stop-color="#00a990"/>
          <stop offset="0.55" stop-color="#00a990"/>
          <stop offset="0.62" stop-color="#f37122"/>
          <stop offset="0.78" stop-color="#f37122"/>
          <stop offset="0.84" stop-color="#00a990"/>
        </linearGradient>
      </defs>
      <rect class="ad-background" width="423" height="587" fill="url(#warmSky)"/>

      <g class="brand-lockup">
        <circle cx="138" cy="58" r="33" fill="none" stroke="var(--purple)" stroke-width="3"/>
        <text class="brand-name" x="182" y="73" font-size="34" textLength="137" lengthAdjust="spacingAndGlyphs">VORRADA</text>
        <text class="brand-name" x="183" y="86" font-size="10.5" textLength="136" lengthAdjust="spacingAndGlyphs">MINDFUL BUSINESS</text>
      </g>

      <text class="headline" x="32" y="176" font-size="76" fill="var(--navy)" textLength="355" lengthAdjust="spacingAndGlyphs">EXPLORE</text>
      <rect x="29" y="183" width="360" height="69" fill="var(--orange)"/>
      <text class="headline" x="40" y="244" font-size="72" fill="var(--white)" textLength="340" lengthAdjust="spacingAndGlyphs">DEVELOP</text>
      <text class="headline" x="31" y="298" font-size="52" fill="var(--sky)" textLength="356" lengthAdjust="spacingAndGlyphs">STRENGTHEN</text>

      <rect x="0" y="315" width="423" height="45" fill="url(#bandPurple)"/>
      <text class="condensed-italic" x="30" y="352" font-size="37" fill="var(--white)" textLength="360" lengthAdjust="spacingAndGlyphs">LEADERSHIP &amp; CULTURE</text>

      <g class="learn-how">
        <path d="M23 400 V378 Q23 372 29 372 H146 L160 400 Z" fill="var(--orange)"/>
        <text class="condensed" x="34" y="394" font-size="20" fill="var(--white)" textLength="106" lengthAdjust="spacingAndGlyphs">LEARN HOW:</text>
        <rect x="24" y="401" width="185" height="73" rx="4" fill="var(--white)" stroke="var(--sky)" stroke-width="1.5"/>
        <path d="M24 405 Q24 401 28 401 H205 Q209 401 209 405 V448 H24 Z" fill="var(--sky)"/>
        <text class="condensed" x="37" y="423" font-size="21" fill="var(--white)" textLength="162" lengthAdjust="spacingAndGlyphs">REAL LEADERSHIP</text>
        <text class="condensed" x="46" y="443" font-size="21" fill="var(--white)" textLength="143" lengthAdjust="spacingAndGlyphs">+ REAL CULTURE</text>
        <text class="condensed" x="41" y="469" font-size="21" fill="var(--blue)" textLength="144" lengthAdjust="spacingAndGlyphs">= REAL RESULTS</text>
      </g>

      <rect x="222" y="380" width="186" height="156" rx="6" fill="url(#teamTones)" opacity="0.9" role="img" aria-label="Silhouettes of four business people standing together, one highlighted in orange"/>

      <g class="footer-wave">
        <path d="M0 500 Q40 540 110 548 Q230 555 300 520 Q360 495 423 498 V587 H0 Z" fill="var(--orange)"/>
        <path d="M0 512 Q40 548 110 555 Q230 562 300 528 Q360 505 423 508 V587 H0 Z" fill="var(--blue)"/>
        <path d="M0 540 Q120 560 200 587 H0 Z" fill="var(--navy)" opacity="0.6"/>
      </g>

      <g class="booth-badge">
        <circle cx="61" cy="532" r="46" fill="none" stroke="var(--orange)" stroke-width="1"/>
        <circle cx="61" cy="532" r="42" fill="var(--orange)"/>
        <text class="condensed" x="34" y="524" font-size="18" fill="var(--ink)" textLength="52" lengthAdjust="spacingAndGlyphs">BOOTH</text>
        <text class="condensed" x="34" y="558" font-size="38" fill="var(--white)" stroke="var(--ink)" stroke-width="1.2" textLength="54" lengthAdjust="spacingAndGlyphs">736</text>
      </g>

      <text class="url" x="129" y="574" font-size="23" textLength="278" lengthAdjust="spacingAndGlyphs">WWW.VMBGROUP.COM</text>
    </svg>
  </section>

  <!-- Option two -->
  <section class="ad second">
    <svg viewBox="0 0 423 587" xmlns="http://www.w3.org/2000/svg">
      <defs>
        <linearGradient id="coolSky" x1="0" y1="0" x2="0" y2="1">
          <stop offset="0" stop-color="#5fe0dc"/>
          <stop offset="0.3" stop-color="#b3efec"/>
          <stop offset="0.55" stop-color="#dff6f2"/>
          <stop offset="0.62" stop-color="#f5f1e6"/>
          <stop offset="1" stop-color="#f3ead8"/>
        </linearGradient>
        <linearGradient id="bandPurpleTwo" x1="0" y1="0" x2="1" y2="0">
          <stop offset="0" stop-color="#57347f"/>
          <stop offset="0.6" stop-color="#6b449b"/>
          <stop offset="1" stop-color="#5a3787"/>
        </linearGradient>
      </defs>
      <rect class="ad-background" width="423" height="587" fill="url(#coolSky)"/>

      <g class="brand-lockup">
        <circle cx="138" cy="58" r="33" fill="none" stroke="var(--purple)" stroke-width="3"/>
        <text class="brand-name" x="182" y="73" font-size="34" textLength="137" lengthAdjust="spacingAndGlyphs">VORRADA</text>
        <text class="brand-name" x="183" y="86" font-size="10.5" textLength="136" lengthAdjust="spacingAndGlyphs">MINDFUL BUSINESS</text>
      </g>

      <text class="headline" x="32" y="176" font-size="76" fill="var(--navy)" textLength="355" lengthAdjust="spacingAndGlyphs">EXPLORE</text>
      <rect x="29" y="183" width="360" height="69" fill="var(--orange)"/>
      <text class="headline" x="40" y="244" font-size="72" fill="var(--white)" textLength="340" lengthAdjust="spacingAndGlyphs">DEVELOP</text>
      <text class="headline" x="31" y="298" font-size="52" fill="var(--sky)" textLength="356" lengthAdjust="spacingAndGlyphs">STRENGTHEN</text>

      <rect x="0" y="315" width="423" height="45" fill="url(#bandPurpleTwo)"/>
      <text class="condensed-italic" x="30" y="352" font-size="37" fill="var(--white)" textLength="360" lengthAdjust="spacingAndGlyphs">LEADERSHIP &amp; CULTURE</text>

      <g class="learn-how">
        <path d="M112 360 H310 L298 390 Q296 396 289 396 H133 Q126 396 124 390 Z" fill="var(--orange)"/>
        <text class="condensed" x="139" y="389" font-size="28" fill="var(--white)" textLength="143" lengthAdjust="spacingAndGlyphs">LEARN HOW</text>
      </g>

      <g class="formula">
        <rect x="51" y="411" width="65" height="51" rx="4" fill="var(--teal)" role="img" aria-label="Icon of a group of business people"/>
        <rect x="201" y="420" width="58" height="38" rx="4" fill="var(--orange)" opacity="0.85" role="img" aria-label="Icon of a handshake"/>
        <rect x="329" y="415" width="45" height="46" rx="23" fill="var(--teal)" role="img" aria-label="Icon of a target with an arrow"/>

        <text class="condensed" x="88" y="493" font-size="24" fill="var(--blue)" text-anchor="middle">REAL</text>
        <text class="condensed" x="88" y="518" font-size="24" fill="var(--blue)" text-anchor="middle" textLength="118" lengthAdjust="spacingAndGlyphs">LEADERSHIP</text>
        <text class="condensed" x="166" y="505" font-size="24" fill="var(--blue)" text-anchor="middle">+</text>
        <text class="condensed" x="235" y="492" font-size="24" fill="var(--blue)" text-anchor="middle">REAL</text>
        <text class="condensed" x="235" y="517" font-size="24" fill="var(--blue)" text-anchor="middle">CULTURE</text>
        <text class="condensed" x="297" y="505" font-size="24" fill="var(--blue)" text-anchor="middle">=</text>
        <text class="condensed" x="359" y="492" font-size="24" fill="var(--blue)" text-anchor="middle">REAL</text>
        <text class="condensed" x="359" y="517" font-size="24" fill="var(--blue)" text-anchor="middle">RESULTS</text>
      </g>

      <g class="footer-bar">
        <rect x="0" y="537" width="423" height="50" fill="var(--blue)"/>
        <path d="M0 537 H115 L131 587 H0 Z" fill="var(--orange)"/>
        <text class="condensed" x="19" y="570" font-size="14" fill="var(--ink)">BOOTH</text>
        <text class="condensed" x="62" y="577" font-size="36" fill="var(--white)" textLength="49" lengthAdjust="spacingAndGlyphs">736</text>
        <g class="globe-icon" fill="none" stroke="var(--white)" stroke-width="1.6">
          <circle cx="143" cy="562" r="9"/>
          <ellipse cx="143" cy="562" rx="4" ry="9"/>
          <line x1="134" y1="562" x2="152" y2="562"/>
        </g>
        <text class="url" x="161" y="571" font-size="22" textLength="245" lengthAdjust="spacingAndGlyphs">WWW.VMBGROUP.COM</text>
      </g>
    </svg>
  </section>

  <p class="caption">2.875 x 4 inch Ad for a Program Guide at Conference with 15,000</p>
</main>
</body>
</html>
```